Flyer for a Business Consultant

I need a one-page description of services. I am a Brennick Certifed Talents Mentor. I do not have a personal website but think I will soon purchase this template https://varlowskins.example/skins/lectern/. I like the larger font, simplicity and larger font. I will attach his pricing flyer which I like - not to overly guide or restrict your creative thinking, but only to give a little perspective. I don't like busy, noisy - I like clarity, simplicity. Here 's the Brennick website which these same traits https://www.brennicktalentshub.example/ and can be a source of ideas and colors.

Target Market(s)

CEOs and Middle Managers in organizations

Industry/Entity Type

Financial Service

Colors

Designer to choose colors to be used in the design.

Requirements
Must have
• Clarity, simplicity, but also strength (not weak or frilly looking)
Nice to have
• Warm color(s), larger/not skinny font
Should not have
• Loud, noisy, busy

```html
<!DOCTYPE html>
<html lang="en">
<head>
<meta charset="UTF-8">
<title>Brennick Certified Talents Mentor – Services Flyer</title>
<link href="https://fonts.googleapis.com/css2?family=Poppins:wght@400;500;600;700&family=Lora:ital,wght@1,600&display=swap" rel="stylesheet">
<style>
  :root {
    --stage: #5f5f5f;
    --paper: #f3f3f2;
    --ink-dark: #1f2323;
    --ink-grey: #6b6b6b;
    --white: #ffffff;
    --band-green: #2fae6a;
    --band-teal: #1f9a9a;
    --band-blue: #2a78c2;
    --rose: #c44d78;
    --plum: #8a4d9c;
    --violet: #6a4aa0;
    --teal: #2a9a8c;
    --green: #38a46e;
  }
  * { box-sizing: border-box; margin: 0; padding: 0; }
  html, body { width: 1200px; height: 834px; overflow: hidden; }
  body {
    background: var(--stage);
    font-family: "Poppins", Arial, sans-serif;
    position: relative;
  }
  .flyer {
    position: absolute;
    left: 291px; top: 17px;
    width: 618px; height: 800px;
    background: var(--paper);
    overflow: hidden;
  }
  .header { position: absolute; left: 0; top: 0; width: 618px; height: 121px; }
  .header-band { position: absolute; left: 0; top: 0; }
  .credential {
    position: absolute; left: 39px; top: 26px;
    width: 255px; height: 70px;
    border: 1px solid #9a9a9a;
    display: flex; align-items: center; gap: 12px;
    padding-left: 20px;
  }
  .credential-square { width: 44px; height: 44px; background: #7d7d7d; flex: none; }
  .credential-name {
    font-weight: 500; font-size: 14px; line-height: 1.25;
    color: var(--ink-grey);
  }
  .contact {
    position: absolute; left: 377px; top: 20px;
    color: var(--white); font-size: 13px; font-weight: 500; line-height: 22.5px;
  }
  .contact-line { display: flex; align-items: center; gap: 14px; }
  .contact-line svg { flex: none; }

  .hero {
    position: absolute; left: 0; top: 121px; width: 618px; height: 424px;
    background: linear-gradient(160deg, #2b2f30 0%, #1d2122 45%, #262a2b 100%);
  }
  .headline {
    position: absolute; left: 0; top: 148px; width: 618px;
    text-align: center; color: var(--white);
    font-weight: 700; font-size: 30px; line-height: 41px;
  }
  .tagline {
    position: absolute; left: 0; top: 254px; width: 618px;
    text-align: center; color: var(--white);
    font-family: "Lora", Georgia, serif; font-style: italic; font-weight: 600; font-size: 16.5px;
  }
  .aims { position: absolute; left: 68px; top: 294px; width: 500px; list-style: none; }
  .aims li {
    position: relative; padding-left: 18px; margin-bottom: 13px;
    color: var(--white); font-weight: 600; font-size: 14.3px; line-height: 20px;
  }
  .aims li::before {
    content: ""; position: absolute; left: 0; top: 0; bottom: 0; width: 6px; background: var(--white);
  }

  .service {
    position: absolute; border-radius: 94px; color: var(--white); text-align: center;
  }
  .service-left { left: 29px; top: 418px; width: 186px; height: 355px;
    background: linear-gradient(180deg, var(--rose) 0%, #b04c80 36%, var(--teal) 36%, var(--green) 100%); }
  .service-mid { left: 215px; top: 407px; width: 187px; height: 376px;
    background: linear-gradient(180deg, var(--teal) 0%, #2c9a86 37%, var(--plum) 37%, var(--violet) 100%);
    box-shadow: 0 4px 10px rgba(0,0,0,.25); }
  .service-right { left: 403px; top: 418px; width: 184px; height: 355px;
    background: linear-gradient(180deg, var(--rose) 0%, #a94d88 36%, var(--teal) 36%, #23918f 100%); }
  .service-icon {
    position: absolute; left: 50%; transform: translateX(-50%);
    width: 46px; height: 46px; border-radius: 6px; background: rgba(255,255,255,.85);
  }
  .service-left .service-icon, .service-right .service-icon { top: 22px; }
  .service-mid .service-icon { top: 20px; }
  .service-title {
    position: absolute; left: 0; width: 100%;
    font-weight: 700; font-size: 15px; line-height: 22px;
  }
  .service-left .service-title, .service-right .service-title { top: 84px; }
  .service-mid .service-title { top: 86px; }
  .service-body {
    position: absolute; left: 50%; transform: translateX(-50%);
    width: 160px; font-size: 10.6px; line-height: 16px; font-weight: 500;
  }
  .service-left .service-body, .service-right .service-body { top: 142px; }
  .service-mid .service-body { top: 146px; }
</style>
</head>
<body>
  <main class="flyer">
    <header class="header">
      <svg class="header-band" width="618" height="121" viewBox="0 0 618 121">
        <defs>
          <linearGradient id="bandGrad" x1="0" y1="1" x2="1" y2="0">
            <stop offset="0" stop-color="#36b35f"/>
            <stop offset="0.5" stop-color="#1f9a9a"/>
            <stop offset="1" stop-color="#2a6fc2"/>
          </linearGradient>
        </defs>
        <polygon points="323,0 618,0 618,121 362,121" fill="url(#bandGrad)"/>
      </svg>
      <div class="credential">
        <span class="credential-square"></span>
        <span class="credential-name">Brennick Certified<br>Talents Mentor</span>
      </div>
      <div class="contact">
        <div>Dorian Kessler</div>
        <div>Brennick Workplace Talents Mentor</div>
        <div class="contact-line">
          <svg width="14" height="11" viewBox="0 0 14 11"><rect x="1" y="1" width="12" height="9" fill="none" stroke="#fff" stroke-width="1.6"/><polyline points="1,1 7,6 13,1" fill="none" stroke="#fff" stroke-width="1.6"/></svg>
          <span>dorian@talentwiseiq.example</span>
        </div>
        <div class="contact-line">
          <svg width="14" height="14" viewBox="0 0 14 14"><path d="M4 1 L6 4 L4.5 5.5 Q5.5 8.5 8.5 9.5 L10 8 L13 10 L11.5 13 Q4 12 1 3 Z" fill="#fff"/></svg>
          <span>555-014-2290</span>
        </div>
      </div>
    </header>

    <section class="hero" role="img" aria-label="Dark photo of a team joining hands over a desk with laptops"></section>

    <h1 class="headline">A Strength-based Approach to<br>Managing Team Effectiveness</h1>
    <p class="tagline">We help teams grow stronger by:</p>
    <ul class="aims">
      <li>Bringing a deep awareness of their strengths and the strengths of their associates.</li>
      <li>Increasing the Team’s communication and sense of partnership.</li>
      <li>Improving employee engagement and effectiveness.</li>
    </ul>

    <article class="service service-left">
      <div class="service-icon" role="img" aria-label="Icon of a speaker at a lectern"></div>
      <h2 class="service-title">Individual sessions</h2>
      <p class="service-body">Conversational feedback and coaching sessions based on Brennick’s TalentScan assessments. These sessions last about an hour and lead to a personalized translation of the results and how their strengths show up in their work and inherent blind spots they bring.</p>
    </article>

    <article class="service service-mid">
      <div class="service-icon" role="img" aria-label="Icon of a head with a lightbulb idea"></div>
      <h2 class="service-title">Strength Discovery<br>Workshop</h2>
      <p class="service-body">A retreat-style Team Workshop in which the team learns each other’s unique Top 5 strengths. The session is very interactive and provides a common language that leads to improved communication and effectiveness. Tailored in 2,3 and 4-hour options are tailored to your Team’s challenges and opportunities.</p>
    </article>

    <article class="service service-right">
      <div class="service-icon" role="img" aria-label="Icon of stacked building blocks"></div>
      <h2 class="service-title">Follow-on modules</h2>
      <p class="service-body">Follow-on is important to make the insights learned to be practical and integrated into the Teams’ approach and workflows. In a debrief session included as part of the workshop, we provide several 15-minute exercise modules for use in regular meetings, and we offer guest facilitated modules of 30- 60 minutes each.</p>
    </article>
  </main>
</body>
</html>
```